Web Design Project

i'm looking for a sleek modern design i can use for a web site that deals with.
Intelligent Data Capture
Accounts Payable Solutions for faster processing based on our scanning solution.
ultimately we are a intelligent scanning software.

here is a great website, that does exactly what we do, and we like to have most of their services and products.

so something in this idea would be great.
www.varnol.com

so i guess i want a good landing/home page which is smartly designed so users will be inclined to leave their information.

and then information pages.

also i dont need any cms for you to include, i only need you to hook the html hooks for RANK Kettle as i already have a CMS and need it to hook in to that, i am including links to that cheat sheet.
so it is easier when included as you create the Theme.

http://www.rankkettle.com/how-to-create-website-template.html
http://www.rankkettle.com/cheat-sheet.html
Updates

Hi Guys sorry for the long pause in design, but here is where we stand.

what ever design i choose, i need that designer to customize a few things for me based on design that was designed.
and i will need designer to match that them to work with RANK Kettle
here is the cheat sheet for the hooks that we need to match and make it work.
if you have any questions let me know.

otherwise i look forward to working with you. and good luck.

Target Market(s)

CFO's AP Managers, mostly ppl who are not Tech freindly

Industry/Entity Type

Software

Requirements
Must have
• i need on home page, the rotating banner should have 1 ability to place clipvane links to show videos, and also ability to add buttons on these rotating banners that will allow forms to pop up take to another page.

```html
<!DOCTYPE html>
<html lang="en">
<head>
<meta charset="utf-8">
<title>Intelligent Data Capture – Home</title>
<link rel="stylesheet" href="https://fonts.googleapis.com/css2?family=Open+Sans:wght@400;600;700&display=swap">
<style>
  :root{
    --ink:#222;
    --muted:#555;
    --soft:#b9b9b9;
    --brand:#1b88b0;
    --brand-light:#1fb0e0;
    --band:#2e2e2e;
    --band-deep:#1d1d1d;
    --paper:#ffffff;
    --line:#d8d8d8;
    --accent-green:#5a9a1a;
  }
  *{box-sizing:border-box;margin:0;padding:0}
  html,body{width:860px;height:1200px;overflow:hidden}
  body{position:relative;background:var(--paper);font-family:"Open Sans",Arial,sans-serif;color:var(--ink)}
  .abs{position:absolute}

  /* utility bar */
  .utility{right:140px;top:19px;display:flex;align-items:center;font-size:9.5px;color:var(--ink);white-space:nowrap}
  .utility a{color:inherit;text-decoration:none;padding:0 4px;border-left:1px solid #999;line-height:11px}
  .utility a:first-of-type{border-left:0}
  .login{margin-left:8px;width:53px;height:13px;background:var(--brand);color:#fff;font-size:10px;text-align:center;line-height:13px}

  /* header */
  .brand{left:150px;top:78px;display:flex;align-items:center;gap:10px}
  .brand-mark{width:38px;height:38px;background:var(--brand)}
  .brand-name{font-size:32px;font-weight:400;color:#444;letter-spacing:.5px}
  .callout{left:580px;top:60px;width:140px;text-align:right}
  .callout-title{font-size:19px;font-weight:600;color:var(--brand);line-height:22px}
  .callout-phone{font-size:13px;font-weight:600;color:var(--ink);line-height:16px}

  /* main nav */
  .main-nav{left:141px;top:127px;width:579px;display:flex;align-items:center;font-size:10px;font-weight:700;color:#111;text-transform:uppercase;white-space:nowrap}
  .main-nav span{padding:0 5px;border-left:1px solid #999;line-height:13px}
  .main-nav span:first-child{padding-left:0;border-left:0}
  .search-box{margin-left:4px;width:69px;height:11px;background:#777;color:#ddd;font-size:8px;line-height:11px;padding-left:12px;font-weight:400;text-transform:none}
  .search-icon{margin-left:4px}

  /* hero */
  .hero-band{left:0;top:144px;width:860px;height:206px;background:linear-gradient(#1f1f1f,#3a3a3a)}
  .hero{left:141px;top:157px;width:578px;height:210px;background:linear-gradient(90deg,#f4f4f4,#e4e4e4);box-shadow:0 2px 4px rgba(0,0,0,.3)}
  .hero-photo{left:0;top:0;width:320px;height:210px;background:linear-gradient(100deg,#efe9e2 0%,#d9cbbb 35%,#b7aca2 60%,#e6e6e6 100%)}
  .hero-copy{left:300px;top:64px;width:268px;text-align:center}
  .hero-lead{font-size:11px;font-weight:600;line-height:13px;color:#222}
  .hero-title{margin-top:8px;font-size:18px;font-weight:600;color:#333}
  .hero-cta{left:392px;top:128px;width:111px;height:26px;background:var(--brand);color:#fff;font-size:14px;font-weight:600;text-align:center;line-height:26px;border-radius:3px}
  .hero-dots{left:428px;top:195px;display:flex;gap:6px}
  .hero-dots i{width:7px;height:7px;border-radius:50%;background:#222;display:block}
  .hero-dots i:first-child{background:#fff;border:1px solid #222}

  /* announcement */
  .notice-row{left:141px;top:393px;width:578px;display:flex;justify-content:center;align-items:center;gap:14px}
  .notice{font-size:10.5px;color:#444;white-space:nowrap}
  .btn-dark{flex:none;width:91px;height:21px;background:#2b2b2b;color:#fff;font-size:11px;font-weight:600;text-align:center;line-height:21px;border-radius:4px}

  /* services */
  .section-title{font-size:13px;font-weight:600;color:var(--brand)}
  .section-sub{font-size:9.5px;color:var(--soft);line-height:12px}
  .services{left:141px;top:438px;width:270px}
  .services p{margin-top:8px;font-size:10px;line-height:11.5px;color:#333;padding-left:2px;width:262px}
  .checklist{list-style:none;margin-top:6px;padding-left:10px}
  .checklist li{display:flex;align-items:center;gap:8px;font-size:10px;color:#333;line-height:14.5px}
  .btn-light{position:absolute;width:100px;height:19px;border:1px solid #ccc;background:linear-gradient(#fff,#eee);font-size:7.5px;color:var(--brand);line-height:17px;padding-left:8px;border-radius:2px}
  .btn-light svg{position:absolute;right:6px;top:6px}

  .video{left:437px;top:442px;width:282px;height:170px;background:linear-gradient(120deg,#4a3a2a,#6a5a44 40%,#3e4a3a 70%,#2a2a2a)}
  .video-play{left:122px;top:63px;width:36px;height:24px;background:rgba(0,0,0,.8);border-radius:5px}
  .video-bar{left:0;top:145px;width:282px;height:25px;background:#1a1a1a}
  .video-progress{left:0;top:145px;width:282px;height:3px;background:#c4141c}
  .video-time{left:66px;top:155px;font-size:8px;color:#ddd}
  .video-source{left:222px;top:154px;font-size:8px;font-weight:600;color:#999}

  /* feature columns */
  .feature{width:190px}
  .feature-photo{width:183px;height:118px;border:1px solid #ddd;box-shadow:0 1px 3px rgba(0,0,0,.15);margin-top:8px;padding:5px;background:#fff}
  .feature-photo div{width:100%;height:100%}
  .feature p{margin-top:10px;width:180px;font-size:8.2px;line-height:11.3px;color:#444}
  .feature .btn-light{left:1px;top:232px}
  .divider{left:141px;top:917px;width:578px;height:1px;background:var(--line)}

  /* footer band */
  .footer{left:0;top:930px;width:860px;height:228px;background:var(--band);border-top:5px solid #555}
  .footer .section-title{color:var(--brand-light)}
  .testimonial{width:238px;font-size:10px;line-height:11.5px;color:#fff}
  .testimonial cite{display:block;text-align:right;font-style:italic;font-weight:600;color:var(--brand-light);margin-top:3px;font-size:10px}
  .tile{width:84px;height:74px;background:linear-gradient(#f0f0f0,#9a9a9a)}
  .bottom-nav{left:0;top:1158px;width:860px;height:42px;background:var(--band-deep);display:flex;justify-content:center;align-items:center;font-size:11px;font-weight:700;color:#fff}
  .bottom-nav span{padding:0 7px;border-left:1px solid #888;line-height:13px}
  .bottom-nav span:first-child{border-left:0}
</style>
</head>
<body>

<nav class="abs utility">
  <a>Careers</a><a>Blog</a><a>Events &amp; Training</a><a>Support</a><a>Contact Us</a><a>Sign Up</a>
  <span class="login">Login</span>
</nav>

<div class="abs brand"><span class="brand-mark"></span><span class="brand-name">logo</span></div>
<div class="abs callout">
  <div class="callout-title">Call us now</div>
  <div class="callout-phone">1800 - company</div>
</div>

<nav class="abs main-nav">
  <span>Home</span><span>Products &amp; Features</span><span>Pricing</span><span>CMB Centre</span><span>Partners</span><span>Tour</span><span>FAQ's</span><span>Search</span>
  <div class="search-box">Search site</div>
  <svg class="search-icon" width="16" height="14" viewBox="0 0 16 14"><circle cx="6" cy="6" r="4.5" fill="none" stroke="#333" stroke-width="1.6"/><line x1="9.3" y1="9.3" x2="14.5" y2="13" stroke="#333" stroke-width="2"/></svg>
</nav>

<div class="abs hero-band"></div>
<section class="abs hero">
  <div class="abs hero-photo" role="img" aria-label="Photo of a smiling team of business people in suits"></div>
  <div class="abs hero-copy">
    <div class="hero-lead">Store your payroll information in one place and access them any time.</div>
    <div class="hero-title">Easy sign-up with 1 step</div>
  </div>
  <div class="abs hero-cta">TRY NOW</div>
  <div class="abs hero-dots"><i></i><i></i><i></i><i></i></div>
</section>

<div class="abs notice-row">
  <div class="notice">Check out our events and training page for compliance courses, demos and more!</div>
  <div class="btn-dark">Learn More</div>
</div>

<section class="abs services">
  <h2 class="section-title">Make you life easier with our services!</h2>
  <p>Lorem Ipsum is simply dummy text of the printing and typesetting industry. Lorem Ipsum has been the industry's standard dummy text ever since the 1500s.</p>
  <ul class="checklist">
    <li><svg width="14" height="11" viewBox="0 0 14 11"><path d="M1 6l4 4 8-9" fill="none" stroke="var(--accent-green)" stroke-width="2.6"/></svg>When an unknown printer</li>
    <li><svg width="14" height="11" viewBox="0 0 14 11"><path d="M1 6l4 4 8-9" fill="none" stroke="var(--accent-green)" stroke-width="2.6"/></svg>Took a galley of type and scrambled</li>
    <li><svg width="14" height="11" viewBox="0 0 14 11"><path d="M1 6l4 4 8-9" fill="none" stroke="var(--accent-green)" stroke-width="2.6"/></svg>Lorem Ipsum is simply dummy text</li>
    <li><svg width="14" height="11" viewBox="0 0 14 11"><path d="M1 6l4 4 8-9" fill="none" stroke="var(--accent-green)" stroke-width="2.6"/></svg>Of the printing and typesetting</li>
    <li><svg width="14" height="11" viewBox="0 0 14 11"><path d="M1 6l4 4 8-9" fill="none" stroke="var(--accent-green)" stroke-width="2.6"/></svg>Dummy text ever since the 1500s</li>
  </ul>
</section>
<div class="btn-light" style="left:146px;top:589px">Learn More<svg width="12" height="5" viewBox="0 0 12 5"><path d="M0 2.5h11M8 0.5l3 2-3 2" fill="none" stroke="var(--brand)" stroke-width=".8"/></svg></div>

<div class="abs video" role="img" aria-label="Video still of a presenter seated in an office with bookshelves">
  <div class="abs video-play"><svg width="36" height="24" viewBox="0 0 36 24"><path d="M14 6l10 6-10 6z" fill="#fff"/></svg></div>
  <div class="abs video-bar"></div>
  <div class="abs video-progress"></div>
  <svg class="abs" style="left:14px;top:154px" width="60" height="10" viewBox="0 0 60 10"><path d="M0 0l8 5-8 5z" fill="#bbb"/><path d="M28 3h3l4-3v10l-4-3h-3z" fill="#bbb"/></svg>
  <div class="abs video-time">0:00</div>
  <svg class="abs" style="left:205px;top:155px" width="10" height="10" viewBox="0 0 10 10"><circle cx="5" cy="5" r="4" fill="none" stroke="#999" stroke-width="1.2"/></svg>
  <div class="abs video-source">clipvane</div>
  <svg class="abs" style="left:261px;top:155px" width="10" height="10" viewBox="0 0 10 10"><path d="M1 3V1h2M7 1h2v2M9 7v2H7M3 9H1V7" fill="none" stroke="#bbb" stroke-width="1.2"/></svg>
</div>

<section class="abs feature" style="left:141px;top:644px">
  <h2 class="section-title">Our Products</h2>
  <div class="section-sub">What we do</div>
  <div class="feature-photo"><div role="img" aria-label="Photo of a laughing man" style="background:linear-gradient(90deg,#c9a68a,#7a5a44 50%,#d8e0ea)"></div></div>
  <p>Sed ut perspiciatis unde omnis iste natus error sit voluptatem accusantium doloremque laudantium, totam rem aperiam, eaque ipsa quae ab illo inventore veritatis et quasi architecto beatae vitae dicta sunt</p>
  <div class="btn-light">Learn More<svg width="12" height="5" viewBox="0 0 12 5"><path d="M0 2.5h11M8 0.5l3 2-3 2" fill="none" stroke="var(--brand)" stroke-width=".8"/></svg></div>
</section>

<section class="abs feature" style="left:338px;top:644px">
  <h2 class="section-title">Our Partners</h2>
  <div class="section-sub">Our Clients</div>
  <div class="feature-photo"><div role="img" aria-label="Photo of a thoughtful man in profile" style="background:linear-gradient(90deg,#f4f4f4,#e2cbb6 55%,#b08a6c)"></div></div>
  <p>Nemo enim ipsam voluptatem quia voluptas sit aspernatur aut odit aut fugit, sed quia consequuntur magni dolores eos qui ratione voluptatem sequi nesciun tdolore magnam aliquam quaerat voluptatem.</p>
  <div class="btn-light">Learn More<svg width="12" height="5" viewBox="0 0 12 5"><path d="M0 2.5h11M8 0.5l3 2-3 2" fill="none" stroke="var(--brand)" stroke-width=".8"/></svg></div>
</section>

<section class="abs feature" style="left:535px;top:644px">
  <h2 class="section-title">Our Blog</h2>
  <div class="section-sub">Stay tuned for our news</div>
  <div class="feature-photo"><div role="img" aria-label="Photo of a smiling woman holding glasses" style="background:linear-gradient(90deg,#e8e8e8,#e4c6ae 45%,#d7b49a 70%,#f0f0f0)"></div></div>
  <p>Neque porro quisquam est, qui dolorem ipsum quia dolor sit amet, consectetur, adipisci velit, sed quia non numquam eius modi tempora incidunt ut labore et dolore magnam aliquam quaerat voluptatem.</p>
  <div class="btn-light">Learn More<svg width="12" height="5" viewBox="0 0 12 5"><path d="M0 2.5h11M8 0.5l3 2-3 2" fill="none" stroke="var(--brand)" stroke-width=".8"/></svg></div>
</section>

<div class="abs divider"></div>

<footer class="abs footer">
  <h2 class="abs section-title" style="left:142px;top:17px">Testimonials</h2>
  <blockquote class="abs testimonial" style="left:141px;top:48px">Lorem Ipsum is simply dummy text of the printing and typesetting industry. Lorem Ipsum has been the industry's standard dummy text ever since the 1500s.<cite>Martha B.</cite></blockquote>
  <blockquote class="abs testimonial" style="left:141px;top:122px">Lorem Ipsum is simply dummy text of the printing and typesetting industry. Lorem Ipsum has been the industry's standard dummy text ever since the 1500s.<cite>Antony j.</cite></blockquote>

  <h2 class="abs section-title" style="left:436px;top:17px">Partners</h2>
  <div class="abs tile" style="left:424px;top:44px" role="img" aria-label="Photo of a businessman on the phone"></div>
  <div class="abs tile" style="left:519px;top:44px" role="img" aria-label="Photo of a businessman on the phone"></div>
  <div class="abs tile" style="left:611px;top:44px" role="img" aria-label="Photo of a smiling businessman with colleagues"></div>
  <div class="abs tile" style="left:424px;top:127px;background:linear-gradient(#eee,#444)" role="img" aria-label="Photo of business people giving thumbs up"></div>
  <div class="abs tile" style="left:519px;top:127px;background:linear-gradient(#eee,#444)" role="img" aria-label="Photo of business people giving thumbs up"></div>
  <div class="abs tile" style="left:611px;top:127px" role="img" aria-label="Photo of a support agent with headset"></div>
</footer>

<nav class="abs bottom-nav">
  <span>HOME</span><span>PRODUCTS &amp; FEATURES</span><span>PRICING</span><span>CMB CENTRE</span><span>PARTNERS</span><span>TOUR</span><span>FAQ'S</span>
</nav>

</body>
</html>
```